Business Card Design For A Renovation Contractor Company

We need a business card for a new company based in Singapore, our company name is "KT Planora". We are a renovation contractor that builds designs into reality. We build more of F&B restaurants, retail stores and commercial offices. We work very closely with designers. The final design should communicate to our client that we are a company that you can trust, that will plan and complete your project without giving you a headache. I like my client to remember my company as "KT". The beauty of SIMPLE is important.

Industry/Entity Type

Contractor

Requirements
Nice to have
• Black or Red base

```html
<!DOCTYPE html>
<html lang="en">
<head>
<meta charset="utf-8">
<title>KT Planora – Business Card</title>
<link href="https://fonts.googleapis.com/css2?family=Arimo:wght@400;700&display=swap" rel="stylesheet">
<style>
  :root {
    --page-bg: #f6e3e3;
    --card-deep: #5e1418;
    --card-mid: #9a2228;
    --card-bright: #e0323c;
    --name-white: #f7eeee;
    --ink-dark: #1e0f11;
    --card-shadow: rgba(70, 20, 24, 0.28);
  }

  * { margin: 0; padding: 0; box-sizing: border-box; }

  html, body {
    width: 1200px;
    height: 960px;
    overflow: hidden;
    background: var(--page-bg);
  }

  .canvas {
    position: relative;
    width: 1200px;
    height: 960px;
    display: flex;
    align-items: center;
    justify-content: center;
  }

  .business-card {
    position: relative;
    width: 1000px;
    height: 680px;
    overflow: hidden;
    box-shadow: 0 18px 40px var(--card-shadow);
    font-family: "Arimo", Arial, sans-serif;
  }

  .card-pattern {
    position: absolute;
    inset: 0;
    background:
      radial-gradient(ellipse 40% 55% at 30% 30%, var(--card-bright) 0%, transparent 70%),
      radial-gradient(ellipse 35% 50% at 92% 62%, var(--card-bright) 0%, transparent 70%),
      linear-gradient(120deg, var(--card-deep) 0%, var(--card-mid) 45%, var(--card-deep) 75%, var(--card-mid) 100%);
  }

  .brand-mark {
    position: absolute;
    left: 350px;
    top: 70px;
    font-size: 104px;
    font-weight: 700;
    letter-spacing: 4px;
    line-height: 1;
    color: var(--ink-dark);
  }

  .company-name {
    position: absolute;
    left: 250px;
    top: 235px;
    font-size: 112px;
    font-weight: 400;
    line-height: 1;
    color: var(--name-white);
    white-space: nowrap;
  }

  .tagline {
    position: absolute;
    left: 110px;
    top: 420px;
    font-size: 62px;
    font-weight: 700;
    line-height: 1;
    color: var(--ink-dark);
    white-space: nowrap;
  }
</style>
</head>
<body>
  <main class="canvas">
    <section class="business-card">
      <div class="card-pattern" role="img" aria-label="Red gradient background with flowing dotted swirl lines in red, white and black"></div>
      <div class="brand-mark">KT</div>
      <h1 class="company-name">KT Planora</h1>
      <p class="tagline">building reality with a plan</p>
    </section>
  </main>
</body>
</html>
```